Breakfast Briefings / Lunch & Learn

I would like to have a double sided flyer size 8x10 to display the breakfast briefing on one side and Lunch & Learn on the other side.

Header on each side to say
2018 Calendar Breakfast Briefing (on the breakfast side)
2018 Calendar Lunch & Learn (on the lunch side)

I have attached a copy of the files we would like to use.

Learn

```html
<!DOCTYPE html>
<html lang="en">
<head>
<meta charset="utf-8">
<title>2018 Calendar – Lunch &amp; Learn / Breakfast Briefing</title>
<link rel="stylesheet" href="https://fonts.googleapis.com/css2?family=Montserrat:wght@400;500;600&family=Roboto+Condensed:wght@700&display=swap">
<style>
  :root {
    --page-bg: #dcdcdc;
    --band-blue: #0a6aa1;
    --title-cyan: #5cc3ec;
    --month-blue: #0e6aa3;
    --topic-grey: #555a5e;
    --rule-grey: #9a9a9a;
    --accent-orange: #e8652a;
    --brand-grey: #5d6368;
    --brand-blue: #1d7bbf;
    --name-ink: #1f1f1f;
    --row1: #e8452a;
    --row2: #6fb536;
    --row3: #2d8fd0;
    --row4: #c43f8c;
  }
  * { box-sizing: border-box; margin: 0; padding: 0; }
  html, body { width: 1200px; height: 1200px; overflow: hidden; }
  body {
    background: var(--page-bg);
    font-family: "Montserrat", Arial, sans-serif;
    position: relative;
  }
  .flyer {
    position: absolute;
    top: 248px;
    width: 565px;
    height: 704px;
    background: radial-gradient(ellipse at 50% 50%, #f7f7f7 0%, #e4e4e4 70%, #d9d9d9 100%);
    box-shadow: 0 4px 10px rgba(0,0,0,.35);
    overflow: hidden;
  }
  .flyer--lunch { left: 24px; }
  .flyer--breakfast { left: 611px; }

  .flyer__header {
    position: absolute;
    top: 19px; left: 0; right: 0;
    height: 135px;
    background: var(--band-blue);
    text-align: center;
  }
  .flyer__year {
    position: absolute;
    top: 8px; left: 0; right: 0;
    font-weight: 600;
    font-size: 57px;
    letter-spacing: 2px;
    color: var(--title-cyan);
    line-height: 1;
  }
  .flyer__rule {
    position: absolute;
    top: 72px; left: 46px; right: 46px;
    height: 3px;
    background: var(--title-cyan);
  }
  .flyer__series {
    position: absolute;
    top: 82px; left: 0; right: 0;
    font-weight: 500;
    font-size: 47px;
    color: #fff;
    line-height: 1;
  }

  /* Lunch & Learn list */
  .topics { position: absolute; top: 161px; left: 56px; width: 484px; list-style: none; }
  .topics__row {
    display: flex;
    align-items: center;
    height: 37.6px;
    border-bottom: 1px dashed var(--rule-grey);
    font-size: 16px;
  }
  .topics__row:last-child { border-bottom: none; }
  .topics__month { width: 94px; text-align: right; color: var(--month-blue); font-weight: 500; }
  .topics__title { margin-left: 25px; color: var(--topic-grey); font-weight: 500; white-space: nowrap; }
  .topics__title sup { font-size: 9px; }

  .tagline {
    position: absolute;
    top: 550px; left: 0; right: 0;
    text-align: center;
    font-size: 24px;
    color: var(--accent-orange);
    letter-spacing: 1px;
  }
  .brand {
    position: absolute;
    display: flex;
    align-items: center;
    gap: 10px;
    font-weight: 500;
    color: var(--brand-grey);
    letter-spacing: 4px;
  }
  .brand__mark { background: var(--brand-blue); }
  .flyer--lunch .brand { top: 612px; left: 0; right: 0; justify-content: center; font-size: 40px; }
  .flyer--lunch .brand__mark { width: 30px; height: 30px; }
  .flyer--breakfast .brand { top: 622px; right: 14px; font-size: 18px; letter-spacing: 2px; gap: 6px; }
  .flyer--breakfast .brand__mark { width: 14px; height: 14px; }

  .flyer__footer {
    position: absolute;
    left: 0; right: 0; bottom: 0;
    height: 44px;
    background: var(--band-blue);
  }

  .timeline { position: absolute; top: 0; left: 0; width: 565px; height: 704px; }
  .timeline .month { font-family: "Montserrat", Arial, sans-serif; font-size: 11.5px; font-weight: 500; }
  .timeline .dept { font-family: "Montserrat", Arial, sans-serif; font-size: 9.5px; font-weight: 500; fill: #fff; text-anchor: middle; }
  .timeline .host { font-family: "Roboto Condensed", "Arial Narrow", sans-serif; font-size: 11.5px; font-weight: 700; fill: var(--name-ink); text-anchor: middle; }
  .m1 { fill: var(--row1); } .m2 { fill: var(--row2); } .m3 { fill: var(--row3); } .m4 { fill: var(--row4); }
</style>
</head>
<body>

<section class="flyer flyer--lunch">
  <header class="flyer__header">
    <h1 class="flyer__year">2018 CALENDAR</h1>
    <div class="flyer__rule"></div>
    <h2 class="flyer__series">Lunch &amp; Learn</h2>
  </header>
  <ul class="topics">
    <li class="topics__row"><span class="topics__month">March</span><span class="topics__title">Mindfulness</span></li>
    <li class="topics__row"><span class="topics__month">April</span><span class="topics__title">Nutrition and Lifestyle Coaching</span></li>
    <li class="topics__row"><span class="topics__month">May</span><span class="topics__title">What is Neuromodulation</span></li>
    <li class="topics__row"><span class="topics__month">June</span><span class="topics__title">Achieve Your Goals</span></li>
    <li class="topics__row"><span class="topics__month">July</span><span class="topics__title">Changing Your Life with Positive Thinking</span></li>
    <li class="topics__row"><span class="topics__month">August</span><span class="topics__title">What is Clean Eating and How Do I get Started</span></li>
    <li class="topics__row"><span class="topics__month">September</span><span class="topics__title">Budgeting 101 Financial Wellness</span></li>
    <li class="topics__row"><span class="topics__month">October</span><span class="topics__title">Busted Nutrition Myths</span></li>
    <li class="topics__row"><span class="topics__month">November</span><span class="topics__title">Time Management : No time like present</span></li>
    <li class="topics__row"><span class="topics__month">December</span><span class="topics__title">1<sup>st</sup> Time Home Buyers</span></li>
  </ul>
  <p class="tagline">LIFE - LONG - LEARN</p>
  <div class="brand"><span class="brand__mark"></span>corvia</div>
</section>

<section class="flyer flyer--breakfast">
  <svg class="timeline" viewBox="0 0 565 704" xmlns="http://www.w3.org/2000/svg">
    <defs>
      <linearGradient id="row1Fill" gradientUnits="userSpaceOnUse" x1="71" y1="0" x2="431" y2="0"><stop offset="0" stop-color="#e8262b"/><stop offset="1" stop-color="#f36f21"/></linearGradient>
      <linearGradient id="turn1Stroke" gradientUnits="userSpaceOnUse" x1="0" y1="210" x2="0" y2="356"><stop offset="0" stop-color="#f7941d"/><stop offset=".5" stop-color="#f2e81b"/><stop offset="1" stop-color="#8dc63f"/></linearGradient>
      <linearGradient id="row2Fill" gradientUnits="userSpaceOnUse" x1="131" y1="0" x2="431" y2="0"><stop offset="0" stop-color="#74c043"/><stop offset="1" stop-color="#8dc63f"/></linearGradient>
      <linearGradient id="turn2Stroke" gradientUnits="userSpaceOnUse" x1="0" y1="340" x2="0" y2="486"><stop offset="0" stop-color="#74c043"/><stop offset="1" stop-color="#45c3e5"/></linearGradient>
      <linearGradient id="row3Fill" gradientUnits="userSpaceOnUse" x1="131" y1="0" x2="431" y2="0"><stop offset="0" stop-color="#3fa9df"/><stop offset="1" stop-color="#2f6db5"/></linearGradient>
      <linearGradient id="turn3Stroke" gradientUnits="userSpaceOnUse" x1="0" y1="470" x2="0" y2="614"><stop offset="0" stop-color="#2f59a8"/><stop offset="1" stop-color="#b23e8e"/></linearGradient>
      <linearGradient id="row4Fill" gradientUnits="userSpaceOnUse" x1="131" y1="0" x2="431" y2="0"><stop offset="0" stop-color="#e2245e"/><stop offset="1" stop-color="#c54592"/></linearGradient>
    </defs>

    <rect x="0" y="154" width="565" height="506" fill="#ffffff" fill-opacity="0" role="img" aria-label="Faint background icons: dollar sign, lightbulb, megaphone and a business team"/>

    <!-- row 1 -->
    <polygon fill="url(#row1Fill)" points="75,210 187,210 195,218 187,226 75,226 71,218"/>
    <polygon fill="url(#row1Fill)" points="199,210 327,210 335,218 327,226 199,226 207,218"/>
    <polygon fill="url(#row1Fill)" points="339,210 431,210 431,226 339,226 347,218"/>
    <path d="M429 218 A65 65 0 0 1 429 348" fill="none" stroke="url(#turn1Stroke)" stroke-width="16"/>
    <!-- row 2 -->
    <polygon fill="url(#row2Fill)" points="431,340 310,340 302,348 310,356 431,356 423,348"/>
    <polygon fill="url(#row2Fill)" points="298,340 205,340 197,348 205,356 298,356 290,348"/>
    <polygon fill="url(#row2Fill)" points="193,340 131,340 131,356 193,356 185,348"/>
    <path d="M131 348 A65 65 0 0 0 131 478" fill="none" stroke="url(#turn2Stroke)" stroke-width="16"/>
    <!-- row 3 -->
    <polygon fill="url(#row3Fill)" points="131,470 205,470 213,478 205,486 131,486"/>
    <polygon fill="url(#row3Fill)" points="217,470 335,470 343,478 335,486 217,486 225,478"/>
    <polygon fill="url(#row3Fill)" points="347,470 431,470 431,486 347,486 355,478"/>
    <path d="M429 478 A64 64 0 0 1 429 606" fill="none" stroke="url(#turn3Stroke)" stroke-width="16"/>
    <!-- row 4 -->
    <polygon fill="url(#row4Fill)" points="431,598 300,598 292,606 300,614 431,614 423,606"/>
    <polygon fill="url(#row4Fill)" points="288,598 190,598 182,606 190,614 288,614 280,606"/>
    <polygon fill="url(#row4Fill)" points="178,598 131,598 131,614 178,614 170,606"/>
    <path d="M133 606 Q72 606 66 660" fill="none" stroke="#e2203f" stroke-width="16"/>

    <!-- row 1 labels -->
    <text class="month m1" x="76" y="202">MARCH</text>
    <text class="month m1" x="199" y="202">APRIL</text>
    <text class="month m1" x="336" y="202">MAY</text>
    <text class="dept" x="131" y="221.5">FINANCE</text>
    <text class="dept" x="263" y="221.5">R &amp; D</text>
    <text class="dept" x="393" y="221.5">OPERATIONS</text>
    <text class="host" x="134" y="240">Tom Hale</text>
    <text class="host" x="260" y="240">Nick Andreadis</text>
    <text class="host" x="387" y="240">Paul Brenner</text>
    <!-- row 2 labels -->
    <text class="month m2" x="120" y="333">AUGUST</text>
    <text class="month m2" x="232" y="333">JULY</text>
    <text class="month m2" x="338" y="333">JUNE</text>
    <text class="dept" x="157" y="351.5">PEPOLE</text>
    <text class="dept" x="262" y="351.5">QUALITY</text>
    <text class="dept" x="388" y="351.5">CLINICAL/REG</text>
    <text class="host" x="153" y="371">Meera Dutta</text>
    <text class="host" x="262" y="371">Daniel Ostrowski</text>
    <text class="host" x="385" y="371">Brian Fenner</text>
    <!-- row 3 labels -->
    <text class="month m3" x="118" y="462">SEPTEMBER</text>
    <text class="month m3" x="226" y="462">OCTOBER</text>
    <text class="month m3" x="333" y="462">NOVEMBER</text>
    <text class="dept" x="154" y="481.5">MARKETING</text>
    <text class="dept" x="270" y="481.5">LEGAL</text>
    <text class="dept" x="390" y="481.5">MARKET ACCESS</text>
    <text class="host" x="158" y="501">Rohan Malik</text>
    <text class="host" x="262" y="501">Tariq Hamdan</text>
    <text class="host" x="381" y="501">Caroline Westerberg</text>
    <!-- row 4 labels -->
    <text class="month m4" x="115" y="590">2019 TBD</text>
    <text class="month m4" x="219" y="590">2019 TBD</text>
    <text class="month m4" x="335" y="590">DECEMBER</text>
    <text class="dept" x="140" y="609.5">SALES</text>
    <text class="dept" x="246" y="609.5">MEDICAL</text>
    <text class="dept" x="360" y="609.5">TOS</text>
    <text class="host" x="143" y="630">Jon Avery</text>
    <text class="host" x="248" y="630">Mark Holloway</text>
    <text class="host" x="370" y="630">Laura Bennett</text>
  </svg>

  <header class="flyer__header">
    <h1 class="flyer__year">2018 CALENDAR</h1>
    <div class="flyer__rule"></div>
    <h2 class="flyer__series">Breakfast Briefing</h2>
  </header>
  <div class="brand"><span class="brand__mark"></span>corvia</div>
  <div class="flyer__footer"></div>
</section>

</body>
</html>
```